Restaurant Menu for Ranveli Restaurant Qatar

I am a restaurant owner. Own 3 restaurants in Qatar and Dubai. I am working on a big restaurant (850 Sq m). Plan to open on 24th February. It's Sri Lankan Restaurant in Qatar.
I feel like keeping Separate menus for 1. Lunch and Dinner 2. Bevarages 3. Breakfast 4. Special deals and items.
Colours: Can be found in the pictures added. The Logo and sign board has been attached.
Food Categories:
1. Rice and Curry
2.Biriyani
3.Chinese like: Fried Rice, Nasi Gorang, Soups, Develled meat & Sea food.
4. Sri Lankan specials: Kottu Roty, Dolphin Kottu, String Hopper Kottu
5. Curries: Chicken, Mutton, Beef, Baabath (Guts), Liver (goat's & Cow's),
6. A variety of Sri Lankan Tea, Coffee
7. Short eats: Samosa, Rolls, Patis, Cutlet, Vadai, Pan Cakr, Lavariya,
8. Range of Bakery Items
9. Fresh Juices & Faluda
10. Biriyani Sawan
11. Sizzlers

Target Market(s)

Middle Class and High

Industry/Entity Type

Asian Restaurant

Font styles to use
Script

Requirements
Must have
• Picture based Menu.
• Beverage Menu : 20cmX18cm, 6 pages, single sheet folded single sheet into 3
• Food Menu: 15cmX30cm or 20cmX36cm, 8 pages, each page will consist 2 pictures, Tiltle of each picture is the Item name and Price., each picture will contain other menu options titled "Choose in Between" { Ex: Beef 10, Mutton 12, Chicken 11, Extra cheese 3}
Nice to have
• 1. Indicate "All Prices are in Qatari Riyal" In the cover Page
• 2. An Icon for Chilly/Hot items
• 3. Restaurant Logo in the Cover and Named "Ranveli Grand"
• 4. Creative Graphics and designs
• 5. A short story of the background and history (for some selected items, specially in the desert, beverage etc)
Should not have
• 1. Bullet point menu
• 2. All similar picture style

```html
<!DOCTYPE html>
<html lang="en">
<head>
<meta charset="utf-8">
<title>Ranveli Restaurant Qatar – Menu</title>
<link rel="stylesheet" href="https://fonts.googleapis.com/css2?family=Raleway:wght@300;400;600&family=Open+Sans:wght@400;600&display=swap">
<style>
  :root {
    --backdrop: #e4e4e4;
    --paper: #ffffff;
    --paper-shade: #f2f2f2;
    --gold: #c4b173;
    --gold-light: #d6c797;
    --gold-dark: #a8945a;
    --text-light: #fbf7ea;
    --text-muted: #f1e9cf;
    --label-orange: #ec8f1e;
    --label-yellow: #f3c316;
    --label-ink: #4a3410;
    --brand-red: #b3282d;
    --ink: #2b2b2b;
  }
  * { box-sizing: border-box; margin: 0; padding: 0; }
  html, body { width: 1200px; height: 900px; overflow: hidden; }
  body {
    background: var(--backdrop);
    font-family: "Open Sans", Arial, sans-serif;
    position: relative;
  }

  /* ---------- Cover ---------- */
  .cover {
    position: absolute; left: 50px; top: 180px;
    width: 370px; height: 540px;
    background: var(--paper);
    box-shadow: 0 6px 18px rgba(0,0,0,.18);
    overflow: hidden;
  }
  .cover__hero {
    position: absolute; left: 0; top: 0; width: 100%; height: 262px;
    background: radial-gradient(ellipse at 55% 60%, #f4f1ea 0 38%, #8a5a34 62%, #5a3620 100%);
  }
  .cover__band {
    position: absolute; left: 0; top: 262px; width: 100%; height: 100px;
    display: flex;
  }
  .cover__title {
    flex: 0 0 205px;
    background: var(--gold);
    color: var(--text-light);
    font-family: "Raleway", Arial, sans-serif;
    font-weight: 300;
    font-size: 44px;
    letter-spacing: 3px;
    display: flex; align-items: center; padding-left: 22px;
  }
  .cover__thumbs { flex: 1; display: flex; gap: 3px; background: var(--paper); padding: 3px 0 3px 3px; }
  .cover__thumb { flex: 1; }
  .cover__thumb--grill { background: linear-gradient(160deg, #d9d2c4, #9c8466 60%, #6d5a42); }
  .cover__thumb--wrap { background: linear-gradient(160deg, #e7d3a8, #b8733e 55%, #5f7a36); }
  .cover__brand {
    position: absolute; left: 34px; top: 430px;
    display: flex; align-items: center; gap: 12px;
    color: var(--ink);
    font-family: "Raleway", Arial, sans-serif;
    font-weight: 600; font-size: 21px;
  }
  .cover__brand-dot { width: 22px; height: 22px; border-radius: 50%; background: var(--brand-red); }

  /* ---------- Spread ---------- */
  .spread {
    position: absolute; left: 450px; top: 180px;
    width: 700px; height: 540px;
    display: flex;
    box-shadow: 0 6px 18px rgba(0,0,0,.18);
  }
  .page {
    position: relative; width: 350px; height: 100%;
    background: var(--paper);
  }
  .page--left { background: linear-gradient(90deg, var(--paper) 80%, var(--paper-shade)); }
  .page--right { background: linear-gradient(90deg, var(--paper-shade), var(--paper) 20%); }

  .panel {
    position: absolute; top: 28px; bottom: 28px;
    width: 290px;
    background: linear-gradient(180deg, var(--gold-light), var(--gold) 45%, var(--gold-dark));
    color: var(--text-light);
    padding: 20px 22px;
  }
  .page--left .panel { left: 26px; }
  .page--right .panel { left: 34px; }

  .panel__title {
    font-family: "Raleway", Arial, sans-serif;
    font-weight: 300; font-size: 30px; letter-spacing: 2px;
    line-height: 1;
  }
  .panel__hours {
    margin-top: 6px; font-size: 7px; letter-spacing: .6px; line-height: 1.4;
    color: var(--text-muted);
  }

  .menu-list { margin-top: 14px; font-size: 9px; }
  .menu-list__row { display: flex; justify-content: space-between; padding: 3px 40px 3px 0; }
  .menu-list__name small { display: block; font-size: 6.5px; color: var(--text-muted); }
  .menu-list__price { width: 34px; text-align: left; }

  .feature-pair { display: flex; gap: 8px; margin-top: 16px; }
  .feature { flex: 1; position: relative; }
  .feature__photo { height: 100px; border: 3px solid var(--paper); }
  .feature__photo--kaliya { background: radial-gradient(circle at 50% 55%, #7a3c1a, #3a1d0e 75%); }
  .feature__photo--sizzler { background: radial-gradient(circle at 50% 55%, #e0582a, #f2d08a 55%, #7a5a2a); }
  .feature__photo--biryani { background: radial-gradient(circle at 50% 50%, #f1ead6, #a8a06c 55%, #4b5530); }
  .feature__photo--seafood { background: radial-gradient(circle at 50% 50%, #f4efe2, #d08a4a 50%, #8c2d22); }
  .feature__label {
    margin: -6px 6px 0; position: relative;
    padding: 3px 4px 4px; text-align: center; color: var(--label-ink);
  }
  .page--left .feature__label { background: var(--label-orange); }
  .page--right .feature__label { background: var(--label-yellow); }
  .feature__name { font-size: 8px; font-weight: 600; letter-spacing: .3px; }
  .feature__choices { font-size: 5.5px; line-height: 1.35; }
  .feature__choices b { font-weight: 600; }
</style>
</head>
<body>

<section class="cover">
  <div class="cover__hero" role="img" aria-label="Photo of grilled meat with roast potatoes and vegetables on a white plate"></div>
  <div class="cover__band">
    <h1 class="cover__title">MENU</h1>
    <div class="cover__thumbs">
      <div class="cover__thumb cover__thumb--grill" role="img" aria-label="Photo of a grilled dish"></div>
      <div class="cover__thumb cover__thumb--wrap" role="img" aria-label="Photo of a filled wrap with salad"></div>
    </div>
  </div>
  <div class="cover__brand">
    <span class="cover__brand-dot"></span>
    <span>Ranveli Restaurant Qatar</span>
  </div>
</section>

<section class="spread">
  <article class="page page--left">
    <div class="panel">
      <h2 class="panel__title">RICE &amp; CURRY</h2>
      <p class="panel__hours">LUNCH 12 NOON TO 3 PM<br>DINNER 7 PM TO 11 PM</p>
      <div class="menu-list">
        <div class="menu-list__row"><span class="menu-list__name">Creme of Tomato</span><span class="menu-list__price">75</span></div>
        <div class="menu-list__row"><span class="menu-list__name">Creme of Mushroom</span><span class="menu-list__price">85</span></div>
        <div class="menu-list__row"><span class="menu-list__name">Hot &amp; Sour Soup</span><span class="menu-list__price">75/80</span></div>
      </div>
      <div class="feature-pair">
        <figure class="feature">
          <div class="feature__photo feature__photo--kaliya" role="img" aria-label="Photo of a dark kaliya curry side dish"></div>
          <figcaption class="feature__label">
            <div class="feature__name">KALIYA SIDE DISH</div>
            <div class="feature__choices"><b>Choose in between</b><br>Beef 10 · Mutton 12 · Chicken 11<br>Extra cheese 3</div>
          </figcaption>
        </figure>
        <figure class="feature">
          <div class="feature__photo feature__photo--sizzler" role="img" aria-label="Photo of a seafood sizzler with vegetables"></div>
          <figcaption class="feature__label">
            <div class="feature__name">SEAFOOD SIZZLER</div>
            <div class="feature__choices"><b>Choose in between</b><br>Beef 10 · Mutton 12 · Chicken 11<br>Extra cheese 3</div>
          </figcaption>
        </figure>
      </div>
      <div class="menu-list">
        <div class="menu-list__row"><span class="menu-list__name">Creme of Tomato</span><span class="menu-list__price">75</span></div>
        <div class="menu-list__row"><span class="menu-list__name">Creme of Mushroom</span><span class="menu-list__price">85</span></div>
        <div class="menu-list__row"><span class="menu-list__name">Hot &amp; Sour Soup<small>Vegetable &amp; Non-vegetable</small></span><span class="menu-list__price">75/80</span></div>
        <div class="menu-list__row"><span class="menu-list__name">Manchow Soup<small>Vegetable &amp; Non-vegetable</small></span><span class="menu-list__price">75/80</span></div>
      </div>
    </div>
  </article>

  <article class="page page--right">
    <div class="panel">
      <h2 class="panel__title">BIRYANI</h2>
      <div class="menu-list">
        <div class="menu-list__row"><span class="menu-list__name">Creme of Tomato</span><span class="menu-list__price">75</span></div>
        <div class="menu-list__row"><span class="menu-list__name">Creme of Mushroom</span><span class="menu-list__price">85</span></div>
        <div class="menu-list__row"><span class="menu-list__name">Hot &amp; Sour Soup</span><span class="menu-list__price">75/80</span></div>
      </div>
      <div class="feature-pair">
        <figure class="feature">
          <div class="feature__photo feature__photo--biryani" role="img" aria-label="Photo of a biryani plate with green curry"></div>
          <figcaption class="feature__label">
            <div class="feature__name">KALIYA SIDE DISH</div>
            <div class="feature__choices"><b>Choose in between</b><br>Beef 10 · Mutton 12 · Chicken 11<br>Extra cheese 3</div>
          </figcaption>
        </figure>
        <figure class="feature">
          <div class="feature__photo feature__photo--seafood" role="img" aria-label="Photo of a seafood biryani with rice"></div>
          <figcaption class="feature__label">
            <div class="feature__name">SEAFOOD SIZZLER</div>
            <div class="feature__choices"><b>Choose in between</b><br>Beef 10 · Mutton 12 · Chicken 11<br>Extra cheese 3</div>
          </figcaption>
        </figure>
      </div>
      <div class="menu-list">
        <div class="menu-list__row"><span class="menu-list__name">Creme of Tomato</span><span class="menu-list__price">75</span></div>
        <div class="menu-list__row"><span class="menu-list__name">Creme of Mushroom</span><span class="menu-list__price">85</span></div>
        <div class="menu-list__row"><span class="menu-list__name">Hot &amp; Sour Soup<small>Vegetable &amp; Non-vegetable</small></span><span class="menu-list__price">75/80</span></div>
        <div class="menu-list__row"><span class="menu-list__name">Manchow Soup<small>Vegetable &amp; Non-vegetable</small></span><span class="menu-list__price">75/80</span></div>
      </div>
    </div>
  </article>
</section>

</body>
</html>
```